Family Owned Construction Company Needs Modern Business Cards

We need a new design for our business cards. We are a family owned construction company, Brantwell Construction, based in Mendon, Vermont and would like to add in our new logo and find a more modern look. We also want to use our old to make sure people know who we are. We do site development, highway, environmental, demolition, utility and aggregate.

Contact Information for Business Card

We want to have the office address, 418 Quarry Ridge Road, Alder Falls, NH 03899 and our phone (802) 555-0137 and fax (802) 555-0164 on there as well. Our website is www.brantwellinc.example. There should be a place for the person's name, title, cell number, and email address on the card. Words that we would like to be associated with our company are honesty, predictable, reliable, integrity, dedicated, built right quality, consistent, whatever it takes, and innovation. Safety is also very important to us.

Font styles to use
Serif
Sans Serif
Other font styles liked:
• Square 721 Extented

Colors
0255a3
ffffff

Requirements
Must have
• Office address, phone number and fax number. New logo with excavator
Nice to have
• That we do site development, highway, environmental, demolition, utility, and aggregate. Both logos

```html
<!DOCTYPE html>
<html lang="en">
<head>
<meta charset="UTF-8">
<title>Brantwell Construction – Business Card</title>
<link rel="stylesheet" href="https://fonts.googleapis.com/css2?family=Arimo:wght@400;700&display=swap">
<style>
  :root {
    --navy: #0f2a5e;
    --brand-blue: #0a62b8;
    --sky: #8fc6f2;
    --paper: #ffffff;
    --ink: #111111;
  }
  * { margin: 0; padding: 0; box-sizing: border-box; }
  html, body { width: 870px; height: 1200px; overflow: hidden; background: var(--paper); }
  body { font-family: "Arimo", Arial, sans-serif; color: var(--ink); position: relative; }

  .card { position: absolute; left: 0; width: 870px; background: var(--paper); overflow: hidden; }
  .card--front { top: 0; height: 550px; }
  .card--back { top: 580px; height: 620px; }

  .band { position: absolute; }
  .band--sky { background: var(--sky); }
  .band--blue { background: var(--brand-blue); }
  .band--navy { background: var(--navy); }

  /* front */
  .brand-front {
    position: absolute; left: 0; right: 0; top: 110px;
    display: flex; align-items: center; justify-content: center; gap: 22px;
  }
  .brand-mark { width: 54px; height: 54px; background: var(--navy); }
  .brand-name {
    color: var(--navy); font-weight: 700; text-transform: uppercase;
    line-height: 1.05; letter-spacing: 1px;
  }
  .brand-front .brand-name { font-size: 50px; }
  .brand-name span { display: block; }
  .brand-name .sub { font-size: 0.6em; letter-spacing: 3px; }

  /* back */
  .person { position: absolute; left: 110px; top: 165px; }
  .person-name { font-size: 34px; font-weight: 400; letter-spacing: 0.5px; }
  .person-role { font-size: 22px; margin-top: 20px; margin-left: 58px; text-transform: uppercase; }

  .brand-back {
    position: absolute; left: 470px; top: 110px;
    display: flex; align-items: center; gap: 16px;
  }
  .brand-back .brand-mark { width: 40px; height: 40px; }
  .brand-back .brand-name { font-size: 34px; }

  .contact { position: absolute; left: 0; right: 0; top: 342px; font-size: 22px; }
  .contact-row { display: flex; justify-content: space-between; padding: 0 90px 0 90px; }
  .contact-office { text-align: center; margin-top: 50px; font-size: 19px; line-height: 32px; }
</style>
</head>
<body>
  <section class="card card--front">
    <div class="brand-front">
      <div class="brand-mark"></div>
      <div class="brand-name"><span>Brantwell</span><span class="sub">Construction Inc.</span></div>
    </div>
    <div class="band band--sky" style="left:0;top:377px;width:870px;height:73px"></div>
    <div class="band band--blue" style="left:0;top:450px;width:280px;height:35px"></div>
    <div class="band band--sky" style="left:280px;top:450px;width:290px;height:35px"></div>
    <div class="band band--navy" style="left:570px;top:450px;width:300px;height:35px"></div>
    <div class="band band--navy" style="left:0;top:485px;width:870px;height:65px"></div>
  </section>

  <section class="card card--back">
    <div class="person">
      <div class="person-name">NAME SURNAME</div>
      <div class="person-role">Profession</div>
    </div>
    <div class="brand-back">
      <div class="brand-mark"></div>
      <div class="brand-name"><span>Brantwell</span><span class="sub">Construction Inc.</span></div>
    </div>

    <div class="band band--sky" style="left:0;top:342px;width:870px;height:173px"></div>
    <div class="band band--blue" style="left:0;top:515px;width:280px;height:35px"></div>
    <div class="band band--sky" style="left:280px;top:515px;width:290px;height:35px"></div>
    <div class="band band--navy" style="left:570px;top:515px;width:300px;height:35px"></div>
    <div class="band band--navy" style="left:0;top:550px;width:870px;height:70px"></div>

    <div class="contact">
      <div class="contact-row" style="margin-top:20px">
        <span>Tel : (802) 555-0199</span>
        <span>Mail : namehere@brantwellinc.example</span>
      </div>
      <div class="contact-office">
        <div>Adress : 418 Quarry Ridge Road, Alder Falls, NH 03899</div>
        <div>Phone : (802) 555-0137 Fax : (802) 555-0164</div>
      </div>
    </div>
  </section>
</body>
</html>
```